Web design for a pet services marketplace

I represent a South American based company: “TORVELIS” which provides a different array of pet related services. As a starting point, I would like to get proposals for 1 page website (plus a general frame for forms, instructions etc) web design job for a dog boarding marketplace. If you could add a logo is desirable.
By a Dog Boarding Marketplace, I mean a community marketplace, very much like an roomswap, but for pet services (initially dog boarding/daycare, but evolving to other services such as dog walkers. The purpose is to bring together dog owners and dog-care providers according to qualifications or characteristics given at time of input and needs of the dog owner given at the time of searching. Providers create a profile, entering certain information requested in forms such as their location, type of house/apt, what type/size of dogs they take, prior experience, as well as a personal introduction and pictures. Providers will set their own rates and calendar availability. Then customers browse, schedule and book and pay online. As it works for similar services, there will be a system of reviews and feedback for each care provider.
As to the website, it should be substantially similar to the following websites: (www.pupstayo.com , www.kelbo.com). It should be simple and straightforward, prioritizing ease of use. I would like for visitors to easily understand how the model works by seeing the home page, and getting pop up explanations by browsing over each main icon or message on the homepage. Therefore, I would try to keep additional pages to a minimum.
As I’m new to this, I would not venture as to how many pages I would need and would defer to your suggestion, according to the examples provided. However, I would like to have a visually striking front end, with dog related pictures or cartoon type images. Icons etc should be fun, and related to dogs, vacations, hotels/lodging, travel, etc. Secondary pages (like enrollment forms, Q&A, etc) could have a clean design, maybe adding some non-obtrusive related imagery.
Please note that attached pictures are , third party property and are for guide only.
Additional info:
In general I want to make a site very much like the examples of pupstayo and kelbo, but i think a better job could be done in terms of design. Please feel free to provide your own ideas.
1. For now, since the site will be new, we would not be including a testimonials section. However, we could use the space , or maybe smaller, with the "spread the love"section for announcing special deals for people who share the project.
2. In the principal section, I would like to see a clean layout. Much like pupstayo does. As an alternative, I would also like to see how it would look like if we handled more cartoon type drawings instead of pictures (just a suggestion to see how it would look like).
3. Search spaces should be more floating (merging more with background), as in pupstayo, not in larger boxes.
Updates
Please find in the attachments a very rough wire frame that i just did as response to a project proposal. Please note where i say OK (top and bottom) I mean that those two sections i found ok in such project or the model websites. Pretty regular content in those sections. Added Friday, July 10, 2015
Target Market(s)
dog owners, people who are willing to host pets in their home, kennels
Industry/Entity Type
Pet Care
Number of Pages Required
1 page
Look and feel

```html
<!DOCTYPE html>
<html lang="en">
<head>
<meta charset="utf-8">
<title>TORVELIS – Trusted Dog Sitters</title>
<link rel="stylesheet" href="https://fonts.googleapis.com/css2?family=Open+Sans:wght@300;400;600;700;800&display=swap">
<style>
:root{
  --ink:#3b3f46;
  --muted:#7a7f87;
  --orange:#e0582c;
  --rose:#c99b9b;
  --rose-deep:#b88787;
  --rose-num:#c9a0a0;
  --sky-top:#4f93cf;
  --sky-mid:#8fbde3;
  --sky-light:#c6def1;
  --sand:#ece3d6;
  --navy:#1f5c9a;
  --white:#ffffff;
  --dark:#3a2a24;
  --footer:#ffffff;
  --bar:#5a5f66;
}
*{box-sizing:border-box;margin:0;padding:0}
html,body{width:747px;height:1200px;overflow:hidden}
body{font-family:"Open Sans",Arial,sans-serif;color:var(--ink);background:var(--white)}

/* header */
.site-header{height:82px;display:flex;align-items:center;justify-content:space-between;padding:0 30px 0 86px;background:var(--white)}
.brand{display:flex;align-items:center;gap:10px}
.brand-mark{width:38px;height:38px;border-radius:50%;background:var(--ink)}
.brand-name{font-size:28px;font-weight:700;letter-spacing:1px;color:var(--ink);line-height:1}
.brand-tag{font-size:13px;color:var(--muted);margin-top:3px}
.header-right{display:flex;align-items:center;gap:26px}
.account{display:flex;flex-direction:column;align-items:center;gap:5px}
.account-links{font-size:11px;color:var(--ink)}
.btn-sitter{background:var(--orange);color:var(--white);font-size:10px;padding:4px 9px;border-radius:2px}
.support{text-align:right}
.support small{display:block;font-size:11px;color:var(--ink)}
.support strong{font-size:21px;font-weight:600;color:var(--ink)}

/* hero */
.hero{position:relative;height:330px;overflow:hidden;background:var(--sky-top)}
.hero-art{position:absolute;inset:0;
  background:
    radial-gradient(circle at 62% 40%,rgba(214,232,246,.85) 0,rgba(214,232,246,.35) 22%,rgba(214,232,246,0) 40%),
    radial-gradient(ellipse 55% 30% at 68% 100%,rgba(236,227,214,.95) 0,rgba(236,227,214,.6) 45%,rgba(236,227,214,0) 100%),
    linear-gradient(180deg,var(--sky-top) 0%,var(--sky-mid) 55%,var(--sky-light) 100%)}
.hero-search{position:absolute;left:82px;top:68px}
.hero-search h1{font-size:23px;font-weight:700;color:var(--white);letter-spacing:.5px;margin-bottom:8px}
.search-row{display:flex;gap:6px;margin-bottom:7px}
.field{background:var(--white);border:1px solid #c9d3dc;height:24px;font-size:11px;color:var(--ink);padding:4px 7px}
.field.city{width:200px}
.btn-find{background:var(--navy);color:var(--white);font-size:11px;font-weight:600;padding:5px 10px;height:24px}
.opt{display:flex;align-items:center;gap:4px;background:var(--white);height:22px;padding:0 7px;font-size:10px}
.opt i{width:8px;height:8px;border-radius:50%;border:1px solid var(--ink);display:inline-block}
.date{width:58px;height:22px;font-size:10px;padding:3px 6px}
.arrow{position:absolute;top:145px;width:18px;height:24px;background:rgba(255,255,255,.75);display:flex;align-items:center;justify-content:center}
.arrow.left{left:28px}.arrow.right{right:28px}
.help-tab{position:absolute;right:0;top:150px;width:16px;height:48px;background:var(--orange);color:var(--white);font-size:8px;font-weight:700;writing-mode:vertical-rl;text-align:center;line-height:16px}

/* steps */
.steps{height:238px;display:flex;justify-content:center;gap:24px;padding-top:28px;background:var(--white)}
.step{width:185px;display:flex;align-items:flex-start}
.step-num{font-size:150px;font-weight:300;line-height:.9;color:var(--rose-num)}
.step-body{margin-left:4px;padding-top:4px}
.step-icon{width:64px;height:70px;display:block;margin-bottom:16px}
.step-title{font-size:18px;font-weight:400;color:var(--muted);letter-spacing:.5px}
.step-text{font-size:8px;color:var(--muted);line-height:1.35;margin-top:2px;width:92px}

/* features band */
.features{height:208px;background:var(--rose);display:flex;justify-content:center;gap:34px;padding-top:30px}
.feature{width:190px;text-align:center;color:var(--white)}
.feature-icon{width:64px;height:64px;margin:0 auto 10px;display:block}
.feature h2{font-size:21px;font-weight:700}
.feature p{font-size:8px;opacity:.9;margin-top:2px}

/* share */
.share{position:relative;height:192px;background:var(--dark);overflow:hidden}
.share-photo{position:absolute;left:260px;top:0;right:0;bottom:0;background:radial-gradient(ellipse at 55% 55%,#a66a3e 0,#6e4128 40%,rgba(58,42,36,0) 75%)}
.share-copy{position:absolute;left:50px;top:32px;color:var(--white)}
.share-copy h2{font-size:33px;font-weight:700;line-height:1.1}
.share-copy p{font-size:12px;line-height:1.35;margin-top:4px;width:290px}
.btn-share{display:inline-block;margin-top:12px;background:var(--orange);color:var(--white);font-size:12px;font-weight:600;padding:6px 18px;letter-spacing:.5px}

/* footer */
.site-footer{height:128px;display:flex;gap:30px;padding:20px 0 0 58px;background:var(--footer)}
.foot-col h3{font-size:8px;font-weight:700;margin-bottom:6px;color:var(--ink)}
.foot-col ul{list-style:none}
.foot-col li{font-size:8px;color:var(--ink);line-height:1.45}
.foot-col.links{width:120px}
.news p{font-size:7px;color:var(--ink);margin-bottom:6px}
.news-form{display:flex}
.news-form .email{width:118px;height:16px;border:1px solid #ccc;font-size:7px;padding:3px 5px;color:var(--muted)}
.news-form .btn{background:var(--ink);color:var(--white);font-size:7px;padding:3px 6px;height:16px}
.news h4{font-size:7px;font-weight:700;margin:10px 0 5px}
.socials{display:flex;gap:6px}
.socials span{width:18px;height:18px;border-radius:50%;background:#8a9db5;display:block}
.bottom-bar{height:30px;background:var(--bar);color:#d9dbde;font-size:7px;text-align:center;line-height:30px}
</style>
</head>
<body>

<header class="site-header">
  <div class="brand">
    <span class="brand-mark"></span>
    <div>
      <div class="brand-name">TORVELIS</div>
      <div class="brand-tag">Trusted Dog Sitters</div>
    </div>
  </div>
  <div class="header-right">
    <div class="account">
      <div class="account-links">Login &nbsp;|&nbsp; Sign Up</div>
      <div class="btn-sitter">Become a Sitter</div>
    </div>
    <div class="support">
      <small>Customer Support</small>
      <strong>888-555-0142</strong>
    </div>
  </div>
</header>

<section class="hero">
  <div class="hero-art" role="img" aria-label="Cartoon banner: dogs with suitcases and a beach ball in front of a pet hotel, a globe and a hot-air balloon in a blue sky"></div>
  <div class="hero-search">
    <h1>FIND A LOVING DOG SITTER</h1>
    <div class="search-row">
      <div class="field city">City</div>
      <div class="btn-find">FIND SITTER</div>
    </div>
    <div class="search-row">
      <div class="opt"><i></i>Over Night</div>
      <div class="opt"><i></i>Day Care</div>
      <div class="field date">Start</div>
      <div class="field date">End</div>
    </div>
  </div>
  <div class="arrow left"><svg width="8" height="12" viewBox="0 0 8 12"><path d="M7 1 2 6l5 5" fill="none" stroke="#3b3f46" stroke-width="2"/></svg></div>
  <div class="arrow right"><svg width="8" height="12" viewBox="0 0 8 12"><path d="M1 1l5 5-5 5" fill="none" stroke="#3b3f46" stroke-width="2"/></svg></div>
  <div class="help-tab">HELP</div>
</section>

<section class="steps">
  <div class="step">
    <div class="step-num">1</div>
    <div class="step-body">
      <svg class="step-icon" viewBox="0 0 64 70"><circle cx="26" cy="28" r="16" fill="none" stroke="#b88787" stroke-width="6"/><path d="M38 40l16 18" stroke="#b88787" stroke-width="8" stroke-linecap="round"/></svg>
      <div class="step-title">SEARCH</div>
      <div class="step-text">Browse loving, trusted dog sitters near you.</div>
    </div>
  </div>
  <div class="step">
    <div class="step-num">2</div>
    <div class="step-body">
      <svg class="step-icon" viewBox="0 0 64 70"><rect x="8" y="22" width="48" height="40" rx="5" fill="#b88787"/><rect x="22" y="12" width="20" height="12" rx="3" fill="none" stroke="#b88787" stroke-width="4"/><rect x="8" y="36" width="48" height="4" fill="#f3e3e3"/></svg>
      <div class="step-title">BOOK</div>
      <div class="step-text">Get to know your sitter then book and pay.</div>
    </div>
  </div>
  <div class="step">
    <div class="step-num">3</div>
    <div class="step-body">
      <svg class="step-icon" viewBox="0 0 64 70"><ellipse cx="20" cy="40" rx="11" ry="24" fill="#b88787"/><ellipse cx="46" cy="40" rx="11" ry="24" fill="#b88787"/><path d="M12 30q8 -10 16 0M38 30q8 -10 16 0" fill="none" stroke="#f3e3e3" stroke-width="3"/></svg>
      <div class="step-title">RELAX</div>
      <div class="step-text">You'll get daily photos and updates.</div>
    </div>
  </div>
</section>

<section class="features">
  <div class="feature">
    <svg class="feature-icon" viewBox="0 0 64 64"><circle cx="32" cy="32" r="30" fill="none" stroke="#fff" stroke-width="2"/><path d="M32 14l14 6v12c0 9-6 15-14 18-8-3-14-9-14-18V20z" fill="#fff"/><path d="M25 32l5 5 9-10" fill="none" stroke="#c99b9b" stroke-width="3"/></svg>
    <h2>Insured Pets</h2>
    <p>Reservations include 24/7 customer support</p>
  </div>
  <div class="feature">
    <svg class="feature-icon" viewBox="0 0 64 64"><circle cx="32" cy="32" r="30" fill="#fff"/><ellipse cx="32" cy="38" rx="9" ry="8" fill="#c99b9b"/><circle cx="20" cy="28" r="4" fill="#c99b9b"/><circle cx="27" cy="21" r="4" fill="#c99b9b"/><circle cx="37" cy="21" r="4" fill="#c99b9b"/><circle cx="44" cy="28" r="4" fill="#c99b9b"/></svg>
    <h2>Velted Hosts</h2>
    <p>Vetted by our team</p>
  </div>
  <div class="feature">
    <svg class="feature-icon" viewBox="0 0 64 64"><circle cx="32" cy="32" r="30" fill="none" stroke="#fff" stroke-width="2"/><path d="M32 47l-13-13a8 8 0 0 1 13-10 8 8 0 0 1 13 10z" fill="#fff"/></svg>
    <h2>One On One TLC</h2>
    <p>Your pup stays in their home</p>
  </div>
</section>

<section class="share">
  <div class="share-photo" role="img" aria-label="Photo of a smiling girl hugging a golden spaniel dog"></div>
  <div class="share-copy">
    <h2>Spread the Love</h2>
    <p>Tell a Friend about TORVELIS, and they'll get $10 off their first reservation.</p>
    <span class="btn-share">START SHARING</span>
  </div>
</section>

<footer class="site-footer">
  <div class="foot-col links">
    <h3>HELP</h3>
    <ul><li>Support Center</li><li>How it Works</li><li>Contact Us</li><li>Concierge</li></ul>
  </div>
  <div class="foot-col links">
    <h3>YOU MAY NEED THIS</h3>
    <ul><li>Home</li><li>Contact us</li><li>FAQ</li><li>Terms &amp; conditions</li><li>Privacy policy</li></ul>
  </div>
  <div class="foot-col links">
    <h3>HOSTING</h3>
    <ul><li>Become a Sitter</li><li>How Hosting Works</li><li>Hosting Tips</li><li>Hosting Policy</li></ul>
  </div>
  <div class="foot-col news">
    <h3>NEWS &amp; DEALS BY EMAIL</h3>
    <p>Hear first about our latest news and exclusive deals</p>
    <div class="news-form"><div class="email">Email Address</div><div class="btn">Subscribe</div></div>
    <h4>STAY CONNECTED ON</h4>
    <div class="socials"><span></span><span></span><span></span></div>
  </div>
</footer>
<div class="bottom-bar">© 2015 TORVELIS. All Rights Reserved</div>

</body>
</html>
```